Bonus/Contractor Pack Sticker

Need a sticker for a current promotion we are running. We are a Building Material company which needs a sticker to apply to existing packaging. We would like the design to be visible from a distance and to have the colour Red.

The sticker will be 6" wide by 4" tall and shall be split in the middle to be wrapped around the corner of the box. (as shown in the example)

Words which need to be included on the sticker are
"Bonus 100pcs Lifetime Durable Wedges Inside"

Target Market(s)

Contractors?Do-it Yourselfers

Industry/Entity Type

Construction

Colors
ec1f27

Requirements
Must have
• Red

```html
<!DOCTYPE html>
<html lang="en">
<head>
<meta charset="utf-8">
<title>Bonus Pack Sticker</title>
<link href="https://fonts.googleapis.com/css2?family=Archivo+Black&display=swap" rel="stylesheet">
<style>
  :root {
    --brand-red: #a51f24;
    --paper: #ffffff;
    --wedge-light: #c9544f;
    --wedge-dark: #8f2326;
  }
  html, body {
    margin: 0;
    padding: 0;
    width: 1200px;
    height: 1000px;
    overflow: hidden;
    background: var(--paper);
  }
  .sticker {
    position: absolute;
    left: 172px;
    top: 133px;
    width: 860px;
    height: 574px;
    display: flex;
  }
  .sticker-face {
    width: 430px;
    height: 574px;
    display: block;
  }
  .headline {
    font-family: "Archivo Black", "Arial Black", sans-serif;
    text-anchor: middle;
  }
  .bonus-label { fill: var(--paper); font-size: 40px; }
  .message-line { fill: var(--brand-red); font-size: 51px; }
</style>
</head>
<body>
<div class="sticker">
  <svg class="sticker-face" viewBox="0 0 430 574" xmlns="http://www.w3.org/2000/svg">
    <defs>
      <linearGradient id="wedgeToneLeft" x1="0" y1="0" x2="1" y2="1">
        <stop offset="0" stop-color="var(--wedge-light)"/>
        <stop offset="1" stop-color="var(--wedge-dark)"/>
      </linearGradient>
    </defs>
    <rect class="outer-frame" width="430" height="574" fill="var(--brand-red)"/>
    <rect class="inner-card" x="14" y="14" width="402" height="546" fill="var(--paper)"/>
    <rect class="inner-rule" x="18" y="20" width="392" height="536" fill="none" stroke="var(--brand-red)" stroke-width="4"/>
    <rect class="wedge-photo" role="img" aria-label="Pile of red plastic tile levelling wedges" x="25" y="337" width="374" height="212" fill="url(#wedgeToneLeft)"/>
    <path class="white-sweep" d="M25 330 L25 435 C150 442 330 430 399 337 L399 330 Z" fill="var(--paper)"/>
    <path class="top-banner" d="M25 27 H399 V114 C250 112 80 120 25 215 Z" fill="var(--brand-red)"/>
    <text class="headline bonus-label" x="212" y="87">BONUS 100PCS</text>
    <text class="headline message-line" x="212" y="216">DURABLE</text>
    <text class="headline message-line" x="212" y="278">LIFETIME</text>
    <text class="headline message-line" x="212" y="340">WEDGES</text>
    <text class="headline message-line" x="212" y="401">INSIDE</text>
  </svg>
  <svg class="sticker-face" viewBox="0 0 430 574" xmlns="http://www.w3.org/2000/svg">
    <defs>
      <linearGradient id="wedgeToneRight" x1="0" y1="0" x2="1" y2="1">
        <stop offset="0" stop-color="var(--wedge-light)"/>
        <stop offset="1" stop-color="var(--wedge-dark)"/>
      </linearGradient>
    </defs>
    <rect class="outer-frame" width="430" height="574" fill="var(--brand-red)"/>
    <rect class="inner-card" x="14" y="14" width="402" height="546" fill="var(--paper)"/>
    <rect class="inner-rule" x="18" y="20" width="392" height="536" fill="none" stroke="var(--brand-red)" stroke-width="4"/>
    <rect class="wedge-photo" role="img" aria-label="Pile of red plastic tile levelling wedges" x="25" y="337" width="374" height="212" fill="url(#wedgeToneRight)"/>
    <path class="white-sweep" d="M25 330 L25 435 C150 442 330 430 399 337 L399 330 Z" fill="var(--paper)"/>
    <path class="top-banner" d="M25 27 H399 V114 C250 112 80 120 25 215 Z" fill="var(--brand-red)"/>
    <text class="headline bonus-label" x="212" y="87">BONUS 100PCS</text>
    <text class="headline message-line" x="212" y="216">DURABLE</text>
    <text class="headline message-line" x="212" y="278">LIFETIME</text>
    <text class="headline message-line" x="212" y="340">WEDGES</text>
    <text class="headline message-line" x="212" y="401">INSIDE</text>
  </svg>
</div>
</body>
</html>
```